Flyer für Coaching
Was für ein gewinnbringendes Miteinander. Ich freue mich sehr über diesen gelungenen Flyer - in Postkartenformat. Die Kommunikation war super. Der Designer ist auf alle meine Anmerkungen eingegangen - hat sehr zeitnah reagiert & Geduld bewiesen. Herzlichen Danke für die angenehme Erfahrung.
Zielgruppe
Bei blu4two begleite ich kreativ und individuell auf dem Weg von der Last zur Leichtigkeit - maßgeschneiderte Unterstüzung im 1:1 Verbund supporte ich Personen auf bewusster und unbewusster Ebene (Hypnose/EMDR) dabei im eigenen Leben -> selbstwirksam - selbstwertschätzend zu sein - eigene Potenziale zu entfalten - neue Perspektiven zu entdecken und sich mit Handlungskompetenzen zu bereichern. Meine Zielgruppe sind Erwachsene auf der Suche nach Unterstützung um ihre Herausforderungen zu meistern und nachhaltige Veränderungen für mehr Wohlbefinden & Lebenszufriedenheit zu schaffen. Menschen die sich aktiv mit ihrer persönlichen Entwicklung auseinandersetzen - auseinandersetzen wollen. Z.B. zur Krisenbewältigung, Selbstfürsorge, Gesunderhaltung, Selbstentfaltung.
Headline:
'Selbstbestimmt selbstwirksam leben'
Aufgabenstellung
Ich möchte ein Postkartenformat als Werbeträger - meine derzeitige Karte ist 10,5 cm breit & 14,9 cm hoch mit abgerundeten Ecken - soll die neue auch haben. Vorder- und Rückseite gestaltet - da es eine Werbeträger ist und sie nicht als Postkarte genutzt wir! Ein Handlungsimpuls schon mit einem stimmigen Bild hervorgelockt -> wäre ein Traum. Eine Botschaft mit Nachhaltigkeit - gerne auch so, dass der Leser sie länger aufbewahrt. Alle wichtigen Informationen in kürzester Zeit auf der Vorderseite vermittelt - ich freue mich. Denn Aufmerksamkeit fesselnd + von wem ist die Postkarte - warum bekomme ich sie - schafft Klarheit auf einen Blick. Ich mag Dinge die im Fluss sind - Ecken & scharfe Kanten sind nicht meins. Für den persönlichen Eindruck finde ich ein Bild von mir für den Leser wichtig. Wiedererkennungswert - gerne harmonierend mit meinem Logo welches die Farben #afbd32, #505e68 & #b71673 enthält. Wenn weiß genutzt wird alt-weiß (warmes weiß)bevorzugt.
Sowie den QR-Code auf der Karte einbinden. Ich lege besonderen Wert auf Empathie.
Plaudern & Begegnen - ca. 30 Min. zum Kennenlernen & Fragen klären -> für 0 Euro Einsatz . Dieser Text soll mit drauf - allerdings nicht in den Vordergrund - da es ja eher um den Mehrwert geht
'Wann' eine Person bei mir richtig ist -
'Warum' gerade ich bzw. ein Miteinander ein 'Gewinn' ist. -> Vielleicht hast du Ideen dazu.

```html
<!DOCTYPE html>
<html lang="de">
<head>
<meta charset="utf-8">
<title>blu4two – Selbstbestimmt selbstwirksam leben</title>
<link rel="stylesheet" href="https://fonts.googleapis.com/css2?family=Crimson+Text:wght@400&display=swap">
<style>
  :root {
    --warm-white: #f6f6f2;
    --magenta: #b71673;
    --magenta-soft: #c7538f;
    --slate: #505e68;
    --lime: #afbd32;
  }
  html, body {
    margin: 0;
    padding: 0;
    width: 851px;
    height: 1200px;
    overflow: hidden;
    background: var(--warm-white);
  }
  .card {
    position: relative;
    width: 851px;
    height: 1200px;
    overflow: hidden;
    background: var(--warm-white);
    font-family: "Crimson Text", Georgia, serif;
  }
  .hero-circle {
    position: absolute;
    inset: 0;
  }
  .headline {
    position: absolute;
    left: 24px;
    width: 700px;
    top: 248px;
    margin: 0;
    text-align: center;
    color: #ffffff;
    font-weight: 400;
    font-size: 90px;
    line-height: 95px;
  }
  .brand {
    position: absolute;
    left: 56px;
    top: 1030px;
    display: flex;
    align-items: center;
    gap: 24px;
  }
  .brand-dot {
    width: 76px;
    height: 76px;
    border-radius: 50%;
    background: var(--lime);
  }
  .brand-name {
    margin: 0;
    color: var(--slate);
    font-weight: 400;
    font-size: 72px;
    line-height: 1;
  }
  .footer-band {
    position: absolute;
    left: 0;
    bottom: 0;
    width: 851px;
    height: 41px;
    background: var(--magenta);
  }
</style>
</head>
<body>
  <main class="card">
    <svg class="hero-circle" width="851" height="1200" viewBox="0 0 851 1200" aria-hidden="true">
      <circle cx="306" cy="350" r="488" fill="var(--magenta-soft)"/>
      <circle cx="306" cy="350" r="464" fill="var(--magenta)"/>
    </svg>

    <h1 class="headline">Selbstbestimmt<br>selbstwirksam<br>leben</h1>

    <div class="brand">
      <span class="brand-dot"></span>
      <p class="brand-name">blu4two</p>
    </div>

    <div class="footer-band"></div>
  </main>
</body>
</html>
```